Doctor Formulated Medical Cosmetics

Orvan Kesto is an E-commerce site for high end Medical Cosmetics designed to treat specific skin problems. The Orvan Kesto difference/advantage is that all creams and serums are:
Doctor Formulated, Freshly Handmade, Registered Pharmacy.
The Site also provides real doctor Dermatology Consultations, Library (with a list of - 1. Active Ingredients in the creams with description of their effects, 2. Skin Conditions with information on what causes the condition and typical treatment approaches and outcomes. 3. Resources from Dermatology Journals and literature on the conditions.)
Header Information: Orvan Kesto, languages EN, BG, Register / log in, Shopping Bag. This field should be narrow.
Categories (horizontal): Home, Face, Body, Hair Care, Skin Conditions, Doctor Consultation, Library
The Landing Page should have only one well organized picture, which is intended to create the feeling of luxury, freedom and relaxation. It will be large and will fill the whole screen. All text should be on transparent or similar color fields. Please use the color of the text to create also the feeling of conservative luxury.
Written message / image overlay Orvan Kesto(logo), Skin Care, Doctor Formulated, Freshly Handmade, Registered Pharmacy.
Please study the Landing Page of this site as an example: www.tamerivo.com
Under the Landing Page, there should be a slider with 4 of our products.
Underneath: Four Blog Articles (large pictures for maximum impact and luxury text underneath).
Underneath: Banner for Dermatologist Consultation, (button for Start Your Case Now).
Underneath: Two pictures in a line - Library (with books), and Active Ingredients.
Footer: Philosophy, Categories, Customer Care
Please adhere to the color palate provided in the pictures (as attachments). Provided are some examples of Web Sites with the desired look and feel. www.brulin.com , www.halvestinemd.com .
Please use different shades of gray, white, beige and gold colors, and black. Our products will be in brown glass jars and bottles to convey the professional, pharmacy made nature of the creams and lotions.
We find the following Front Page very attractive and effective - www.tamerivo.com , with its full page image and overlaying text.
Please have a look at this link for the Landing page.
http://www.plovatrex.com/detail/video/woman-lying-on-a-black-sand-beach-in-a-bikini-stock-footage/31862057
I would like to use it in the animated version to achieve the WOW effect. I have uploaded the jpeg version for it, so you will be able create your design.
For the Landing page design, please use only the two uploaded pictures of a woman laying at the beach. Let's see how each of them will look like.
Thank you for your help.
Club
1 page

```html
<!DOCTYPE html>
<html lang="en">
<head>
<meta charset="utf-8">
<title>Orvan Kesto – Doctor Formulated Medical Cosmetics</title>
<link rel="stylesheet" href="https://fonts.googleapis.com/css2?family=Oswald:wght@400;500&family=Roboto:wght@400;500;700&display=swap">
<style>
:root{
  --gold:#cfae66;
  --gold-deep:#b8924a;
  --gold-text:#c9a152;
  --ink:#1b1b1b;
  --text:#333333;
  --muted:#6f6f6f;
  --paper:#ffffff;
  --mist:#f5f5f5;
  --mist-2:#f0f0f0;
  --line:#e2e2e2;
  --footer:#1e1e1e;
  --taupe:#a99385;
}
*{box-sizing:border-box;margin:0;padding:0}
html,body{width:1200px;height:2643px;overflow:hidden}
body{position:relative;background:var(--paper);font-family:"Roboto",Arial,sans-serif;color:var(--text)}
a{color:inherit;text-decoration:none}

/* brand lockup */
.brand{display:flex;align-items:center;gap:12px;color:#fff;font-family:"Roboto",Arial,sans-serif;font-weight:400;letter-spacing:.5px}
.brand-dot{width:40px;height:40px;border-radius:50%;border:2px solid #fff;flex:none}

/* hero */
.hero{position:absolute;left:0;top:0;width:1200px;height:596px;
  background:linear-gradient(90deg,#6b5236 0%,#b08a5c 22%,#caa37a 38%,#7c5e40 55%,#2a2119 70%,#141210 100%)}
.topbar{position:absolute;left:0;top:0;width:1200px;height:85px;background:rgba(0,0,0,.45);display:flex;align-items:center;padding:0 88px}
.topbar .brand{font-size:30px}
.topnav{margin-left:auto;display:flex;align-items:center;gap:0;color:#fff;font-size:14px;text-transform:uppercase}
.topnav .sep{margin:0 12px;opacity:.8}
.burger{width:18px;height:14px;display:flex;flex-direction:column;justify-content:space-between;margin-right:20px}
.burger i{display:block;height:2px;background:#fff}
.lang{display:flex;align-items:center;gap:6px}
.flag{width:16px;height:11px;background:linear-gradient(180deg,#c33 0 50%,#fff 50% 100%);position:relative}
.flag::before{content:"";position:absolute;left:0;top:0;width:7px;height:6px;background:#2b3f8c}
.bag{position:relative;width:32px;height:32px;border-radius:50%;border:2px solid rgba(255,255,255,.6);margin-left:30px;display:flex;align-items:center;justify-content:center}
.bag-count{position:absolute;right:-8px;top:-8px;width:18px;height:18px;border-radius:50%;background:var(--gold);color:#fff;font-size:10px;display:flex;align-items:center;justify-content:center}
.hero-copy{position:absolute;left:819px;top:234px;color:#fff}
.hero-copy .brand{font-size:28px;margin-bottom:24px}
.hero-points{list-style:none;font-family:"Oswald",sans-serif;font-size:25px;line-height:39px;text-transform:uppercase;letter-spacing:.2px}
.hero-points li::before{content:"» ";}
.hero-arrows{position:absolute;left:1026px;top:514px;display:flex;gap:6px}
.round-btn{width:38px;height:38px;border-radius:50%;background:rgba(0,0,0,.75);display:flex;align-items:center;justify-content:center}

/* categories */
.categories{position:absolute;left:0;top:596px;width:1200px;height:54px;background:var(--gold)}
.categories ul{list-style:none;position:relative;height:54px}
.categories li{position:absolute;top:0;height:54px;line-height:54px;color:#fff;font-size:16px;text-transform:uppercase}
.categories li.active{background:var(--gold-deep);text-align:center}

/* headings */
.section-title{text-align:center;font-family:"Oswald",sans-serif;font-weight:400;font-size:27px;color:var(--gold-text);text-transform:uppercase}
.section-sub{text-align:center;font-size:15px;color:var(--muted);margin-top:8px}

/* products */
.products{position:absolute;left:0;top:650px;width:1200px;height:467px;background:linear-gradient(90deg,var(--mist-2) 0 373px,var(--mist) 373px)}
.products .section-title{margin-top:40px}
.product{position:absolute;top:134px;width:220px;text-align:center;transform:translateX(-50%)}
.bottle{width:72px;height:224px;margin:0 auto;border-radius:6px 6px 4px 4px;background:linear-gradient(180deg,#3a3a3a 0 20%,#e0bb98 20%,#d8b18b 100%)}
.product-brand{margin-top:21px;font-size:15px;color:var(--gold-text);text-transform:uppercase}
.product-name{margin-top:6px;font-size:15px;color:var(--ink)}

/* blog */
.blog{position:absolute;left:0;top:1117px;width:1200px;height:786px}
.blog .section-title{margin-top:38px}
.card{position:absolute;width:317px;height:302px;border:1px solid var(--line);background:#fff;box-shadow:0 1px 3px rgba(0,0,0,.06);padding:4px;text-align:center}
.card-img{position:relative;height:172px}
.date{position:absolute;left:1px;top:37px;width:48px;color:#fff;text-align:center}
.date-day{background:var(--gold);height:56px;padding-top:6px;font-size:20px;line-height:22px}
.date-day small{display:block;font-size:10px;text-transform:uppercase}
.date-year{background:var(--ink);height:42px;line-height:42px;font-size:14px}
.card h3{font-weight:400;font-size:16px;color:var(--ink);margin-top:14px}
.card p{font-size:12.5px;line-height:19px;color:var(--muted);margin:10px 14px 0}
.read-more{display:block;margin-top:12px;font-size:13px;color:var(--gold-text)}

/* consultation banner */
.consult{position:absolute;left:0;top:1903px;width:1200px;height:349px;background:linear-gradient(90deg,#a18a7d 0%,#ad978a 50%,#b7a294 100%)}
.consult-photo{position:absolute;right:0;top:0;width:520px;height:349px;background:radial-gradient(ellipse at 55% 45%,#cdb3a0 0%,#b49b8b 45%,rgba(173,151,138,0) 75%)}
.consult-copy{position:absolute;left:88px;top:92px;color:#fff}
.consult-copy .brand{font-size:30px}
.consult-copy h2{font-family:"Oswald",sans-serif;font-weight:400;font-size:35px;text-transform:uppercase;margin-top:18px;letter-spacing:.2px}
.consult-copy p{font-size:21px;line-height:32px;margin-top:6px;width:520px}

/* articles */
.articles{position:absolute;left:0;top:2252px;width:1200px;height:271px}
.articles h2{position:absolute;left:90px;top:46px;font-weight:500;font-size:22px;color:var(--ink);text-transform:uppercase}
.articles-nav{position:absolute;left:1090px;top:50px}
.article{position:absolute;top:90px;display:flex;gap:18px;width:480px}
.article-img{width:160px;height:133px;flex:none}
.article h3{font-weight:400;font-size:14.5px;color:var(--ink);margin-top:6px}
.article .meta{font-size:12px;color:var(--gold-text);margin-top:10px}
.article p{font-size:11.5px;line-height:19.5px;color:var(--muted);margin-top:10px}
.article .read-more{margin-top:4px;font-size:12px}

/* footer */
.site-footer{position:absolute;left:0;top:2523px;width:1200px;height:120px;background:var(--footer);color:#fff}
.footer-links{position:absolute;left:90px;top:46px;font-size:12px}
.footer-links .sep{margin:0 7px}
.copyright{position:absolute;left:90px;top:70px;font-size:12px}
.social{position:absolute;left:967px;top:50px;display:flex;gap:9px}
.social span{width:28px;height:28px;display:block}
</style>
</head>
<body>

<header class="hero">
  <div class="hero-photo" role="img" aria-label="Large hero photograph of a woman with flowing blonde hair against a dark background" style="position:absolute;inset:0"></div>
  <div class="topbar">
    <a class="brand" href="#"><span class="brand-dot"></span>Orvan Kesto</a>
    <nav class="topnav">
      <span class="burger"><i></i><i></i><i></i></span>
      <span class="lang"><span class="flag"></span>English
        <svg width="9" height="6" viewBox="0 0 9 6"><path d="M1 1l3.5 3.5L8 1" stroke="#fff" stroke-width="1.4" fill="none"/></svg></span>
      <span class="sep">|</span><a href="#">Doctor</a>
      <span class="sep">|</span><a href="#">Pharmacy</a>
      <span class="sep">|</span><a href="#">Register</a>
      <span class="sep">|</span><a href="#">Log In</a>
      <span class="bag">
        <svg width="14" height="15" viewBox="0 0 14 15"><rect x="1" y="5" width="12" height="9" fill="#fff"/><path d="M4 5V3.5a3 3 0 016 0V5" stroke="#fff" stroke-width="1.5" fill="none"/></svg>
        <span class="bag-count">0</span>
      </span>
    </nav>
  </div>
  <div class="hero-copy">
    <div class="brand"><span class="brand-dot"></span>Orvan Kesto</div>
    <ul class="hero-points">
      <li>Doctor Formulated</li>
      <li>Freshly Handmade</li>
      <li>Registered Pharmacy</li>
      <li>Highest Ethical Standards</li>
    </ul>
  </div>
  <div class="hero-arrows">
    <span class="round-btn"><svg width="10" height="14" viewBox="0 0 10 14"><path d="M8 1L2 7l6 6" stroke="#fff" stroke-width="2" fill="none"/></svg></span>
    <span class="round-btn"><svg width="10" height="14" viewBox="0 0 10 14"><path d="M2 1l6 6-6 6" stroke="#fff" stroke-width="2" fill="none"/></svg></span>
  </div>
</header>

<nav class="categories">
  <ul>
    <li class="active" style="left:90px;width:111px">Face</li>
    <li style="left:217px">Body</li>
    <li style="left:314px">Hair Care</li>
    <li style="left:453px">Skin Concerns</li>
    <li style="left:585px">Dermatologist</li>
    <li style="left:823px">Consultation</li>
    <li style="left:995px">Library</li>
  </ul>
</nav>

<section class="products">
  <h2 class="section-title">Our Products</h2>
  <p class="section-sub">Lorem Ipsum is simply dummy text of the printing and typesetting industry</p>
  <div class="product" style="left:211px"><div class="bottle" role="img" aria-label="Beige serum bottle with dark cap"></div><div class="product-brand">Orvan Kesto</div><div class="product-name">Neque porro quisquam</div></div>
  <div class="product" style="left:470px;top:139px"><div class="bottle" role="img" aria-label="Beige serum bottle with dark cap"></div><div class="product-brand">Orvan Kesto</div><div class="product-name">Neque porro quisquam</div></div>
  <div class="product" style="left:728px;top:139px"><div class="bottle" role="img" aria-label="Beige serum bottle with dark cap"></div><div class="product-brand">Orvan Kesto</div><div class="product-name">Neque porro quisquam</div></div>
  <div class="product" style="left:983px;top:137px"><div class="bottle" role="img" aria-label="Beige serum bottle with dark cap"></div><div class="product-brand">Orvan Kesto</div><div class="product-name">Neque porro quisquam</div></div>
</section>

<section class="blog">
  <h2 class="section-title">Latest Blog</h2>
  <p class="section-sub">Lorem Ipsum is simply dummy text of the printing and typesetting industry</p>

  <article class="card" style="left:92px;top:132px">
    <div class="card-img" role="img" aria-label="Close-up of glossy brown straight hair" style="background:linear-gradient(135deg,#5a3a26,#a47654 50%,#d2b08e)">
      <div class="date"><div class="date-day">02<small>Jun</small></div><div class="date-year">2016</div></div></div>
    <h3>Neque porro quisquam</h3>
    <p>Lorem ipsum dolor sit amet, consectetur adipiscing elit. Sed blandit massa vel mauris sollicitudin</p>
    <a class="read-more" href="#">Read More »</a>
  </article>
  <article class="card" style="left:439px;top:132px">
    <div class="card-img" role="img" aria-label="Woman with long brown hair on a pale floral backdrop" style="background:linear-gradient(135deg,#eeeae6,#b68a6c 50%,#f1ede9)">
      <div class="date"><div class="date-day">02<small>Jun</small></div><div class="date-year">2016</div></div></div>
    <h3>Neque porro quisquam</h3>
    <p>Lorem ipsum dolor sit amet, consectetur adipiscing elit. Sed blandit massa vel mauris sollicitudin</p>
    <a class="read-more" href="#">Read More »</a>
  </article>
  <article class="card" style="left:788px;top:132px">
    <div class="card-img" role="img" aria-label="Shopper browsing cosmetics shelves in a store" style="background:linear-gradient(135deg,#6b8a5a,#c9c2a8 50%,#e8d6c4)">
      <div class="date"><div class="date-day">02<small>Jun</small></div><div class="date-year">2016</div></div></div>
    <h3>Neque porro quisquam</h3>
    <p>Lorem ipsum dolor sit amet, consectetur adipiscing elit. Sed blandit massa vel mauris sollicitudin</p>
    <a class="read-more" href="#">Read More »</a>
  </article>
  <article class="card" style="left:92px;top:444px">
    <div class="card-img" role="img" aria-label="Woman testing makeup at a cosmetics counter" style="background:linear-gradient(135deg,#3b2e2a,#9a7c6c 50%,#d9ccc4)">
      <div class="date"><div class="date-day">02<small>Jun</small></div><div class="date-year">2016</div></div></div>
    <h3>Neque porro quisquam</h3>
    <p>Lorem ipsum dolor sit amet, consectetur adipiscing elit. Sed blandit massa vel mauris sollicitudin</p>
    <a class="read-more" href="#">Read More »</a>
  </article>
  <article class="card" style="left:439px;top:444px">
    <div class="card-img" role="img" aria-label="Woman surrounded by colourful flowers" style="background:linear-gradient(135deg,#c84a6a,#e7b05a 45%,#9a6ab0)">
      <div class="date"><div class="date-day">02<small>Jun</small></div><div class="date-year">2016</div></div></div>
    <h3>Neque porro quisquam</h3>
    <p>Lorem ipsum dolor sit amet, consectetur adipiscing elit. Sed blandit massa vel mauris sollicitudin</p>
    <a class="read-more" href="#">Read More »</a>
  </article>
  <article class="card" style="left:788px;top:444px">
    <div class="card-img" role="img" aria-label="Woman with windswept wavy auburn hair" style="background:linear-gradient(135deg,#f2ece8,#b06a44 50%,#f4eeea)">
      <div class="date"><div class="date-day">02<small>Jun</small></div><div class="date-year">2016</div></div></div>
    <h3>Neque porro quisquam</h3>
    <p>Lorem ipsum dolor sit amet, consectetur adipiscing elit. Sed blandit massa vel mauris sollicitudin</p>
    <a class="read-more" href="#">Read More »</a>
  </article>
</section>

<section class="consult">
  <div class="consult-photo" role="img" aria-label="Profile portrait of a woman with hair pinned up, bare shoulders"></div>
  <div class="consult-copy">
    <div class="brand"><span class="brand-dot"></span>Orvan Kesto</div>
    <h2>Dermatologist Consultation</h2>
    <p>Doctor Formulated, Freshly Handmade, Registered Pharmacy, Highest Ethical Standards</p>
  </div>
</section>

<section class="articles">
  <h2>Articles</h2>
  <span class="articles-nav"><svg width="24" height="14" viewBox="0 0 24 14"><path d="M7 1L2 7l5 6M17 1l5 6-5 6" stroke="#1b1b1b" stroke-width="1.8" fill="none"/></svg></span>
  <article class="article" style="left:90px">
    <div class="article-img" role="img" aria-label="Two women shopping for beauty products" style="background:linear-gradient(135deg,#d8c4a4,#b0473c 55%,#e6d6c0)"></div>
    <div>
      <h3>Nemo Enim Ipsam Volup</h3>
      <div class="meta">09-07-2016</div>
      <p>Lorem Ipsum has been the industry's standard dummy text ever since the 1500s, when an unknown printer took a galley of type and scrambled it to make a type specimen book.</p>
      <a class="read-more" href="#">Read More &gt;&gt;</a>
    </div>
  </article>
  <article class="article" style="left:624px;top:87px">
    <div class="article-img" role="img" aria-label="Smiling woman holding a skincare jar on a light blue background" style="background:linear-gradient(135deg,#9fd3e8,#e2c6ae 55%,#a8d8ea)"></div>
    <div>
      <h3>Nemo Enim Ipsam Volup</h3>
      <div class="meta">09-07-2016</div>
      <p>Lorem Ipsum has been the industry's standard dummy text ever since the 1500s, when an unknown printer took a galley of type and scrambled it to make a type specimen book.</p>
      <a class="read-more" href="#">Read More &gt;&gt;</a>
    </div>
  </article>
</section>

<footer class="site-footer">
  <div class="footer-links"><a href="#">Privacy Policy</a><span class="sep">|</span><a href="#">Terms of Use</a><span class="sep">|</span><a href="#">About Us</a><span class="sep">|</span><a href="#">Sitemap</a></div>
  <div class="copyright">Copyright © 2016 All Rights</div>
  <div class="social">
    <span style="background:#2aa3db"></span>
    <span style="background:#d8322b"></span>
    <span style="background:#3b5a9a"></span>
    <span style="background:#1a77b0"></span>
  </div>
</footer>

</body>
</html>
```